Mark & Lisa's Hammock Season Party

Invitation to a party 60-80 people at a private residence. Age range 30-40s.

Themes: summer/casual/Australian backyard/local community

**For delivery via both email and printed copy**
Would like one document suitable for both purposes or two versions for electronic or paper invitation. I will arrange printing so please prepare it in a suitable format.

Specimen text attached. Address and phone contact to follow by message with successful bidder

Thanks!
Mark

Target Market(s)

Locals, friends. Party attendees will typicaly be parents in their forties who who be leaving the kids at home for a relaxed party night, and walking home afterward

Industry/Entity Type

Community

Font styles to use
Sans Serif

Requirements
Should not have
• Cliche Australiana imagery. No kangaroos etc

```html
<!DOCTYPE html>
<html lang="en">
<head>
<meta charset="utf-8">
<title>Mark &amp; Lisa's Hammock Season Party – Invitation</title>
<link href="https://fonts.googleapis.com/css2?family=Lato:wght@300;400;700;900&family=Dancing+Script:wght@500;700&display=swap" rel="stylesheet">
<style>
  :root {
    --backdrop: #d3aacb;
    --magenta: #c4147e;
    --magenta-deep: #7a0f63;
    --violet-dark: #2a0a2a;
    --night: #0b040b;
    --white: #ffffff;
    --script-pink: #fbe3f1;
    --ink: #000000;
    --grey-text: #8a8a8a;
    --grey-rule: #5a5a5a;
  }
  * { box-sizing: border-box; margin: 0; padding: 0; }
  html, body { width: 1200px; height: 514px; overflow: hidden; }
  body {
    background: var(--backdrop);
    font-family: "Lato", Arial, sans-serif;
    position: relative;
  }
  .card {
    position: absolute;
    top: 22px;
    width: 348px;
    height: 470px;
    overflow: hidden;
    text-align: center;
    color: var(--white);
  }
  .card--front { left: 218px; }
  .card--back { left: 634px; background: var(--ink); }

  .front-artwork {
    position: absolute; inset: 0;
    background:
      radial-gradient(ellipse 60% 30% at 50% 78%, var(--night) 0%, rgba(11,4,11,0.85) 60%, transparent 100%),
      linear-gradient(180deg, var(--magenta-deep) 0%, var(--magenta) 22%, #b0127a 48%, #6a1068 66%, var(--violet-dark) 82%, var(--night) 100%);
  }
  .line { position: absolute; left: 0; right: 0; }

  .front-kicker { top: 10px; font-weight: 900; font-size: 18px; letter-spacing: 0.2px; }
  .front-lead { top: 32px; font-size: 17px; font-weight: 400; }
  .front-hosts { top: 60px; font-size: 17px; color: var(--ink); font-weight: 400; }
  .front-rule {
    position: absolute; top: 83px; left: 78px; width: 192px; height: 1px;
    background: var(--ink);
  }
  .party-title {
    font-family: "Dancing Script", cursive;
    color: var(--script-pink);
    text-shadow: 0 0 8px rgba(255,180,230,0.6);
    font-weight: 700;
  }
  .title-1 { top: 98px; font-size: 50px; line-height: 1; }
  .title-2 { top: 146px; font-size: 50px; line-height: 1; }
  .title-3 { top: 196px; font-size: 30px; font-weight: 500; line-height: 1; }
  .front-guests { top: 244px; font-size: 10px; font-weight: 700; }
  .clock-icon { position: absolute; top: 366px; left: 162px; width: 24px; height: 24px; }
  .front-when { top: 400px; font-size: 12px; font-weight: 400; line-height: 16px; }
  .front-where { top: 436px; font-size: 12px; font-weight: 700; line-height: 15px; }

  .detail-head { font-size: 11px; font-weight: 700; }
  .detail-note { font-size: 10px; font-weight: 300; color: var(--grey-text); }
  .d1 { top: 49px; } .d2 { top: 78px; } .d3 { top: 107px; }
  .d4 { top: 136px; } .d5 { top: 165px; } .d6 { top: 194px; } .d7 { top: 222px; }
  .phone-icon { position: absolute; top: 290px; left: 162px; width: 26px; height: 30px; }
  .text-us { top: 336px; font-size: 13px; font-weight: 300; color: var(--grey-text); }
  .back-rule {
    position: absolute; left: 56px; right: 56px; height: 1px; background: var(--grey-rule);
  }
  .r1 { top: 356px; } .r2 { top: 391px; }
  .contacts { top: 366px; font-size: 11px; font-weight: 300; color: var(--grey-text); }
  .bring-friends { top: 405px; font-size: 9.5px; font-weight: 300; color: var(--grey-text); line-height: 14px; padding: 0 40px; }
</style>
</head>
<body>
  <section class="card card--front" aria-label="Invitation front">
    <div class="front-artwork" role="img" aria-label="Glowing magenta mosaic backdrop fading to a dark house silhouette at dusk"></div>
    <p class="line front-kicker">LEAVE THE KIDS AT HOME</p>
    <p class="line front-lead">and Let Your Hair Down At</p>
    <p class="line front-hosts">Mark &amp; Lisa's</p>
    <div class="front-rule"></div>
    <h1 class="line party-title title-1">Hammock</h1>
    <p class="line party-title title-2">Season</p>
    <p class="line party-title title-3">Party</p>
    <p class="line front-guests">For Wattle Grove and friends</p>
    <svg class="clock-icon" viewBox="0 0 24 24" aria-hidden="true">
      <circle cx="12" cy="12" r="10" fill="none" stroke="#fff" stroke-width="1.6"/>
      <path d="M12 6v6h5" fill="none" stroke="#fff" stroke-width="1.6" stroke-linecap="round"/>
    </svg>
    <p class="line front-when">Saturday 2 January<br>From 6pm 'til late</p>
    <p class="line front-where">25 Banksia Street,<br>Wattle Grove</p>
  </section>

  <section class="card card--back" aria-label="Invitation details">
    <p class="line detail-head d1">Child-free event</p>
    <p class="line detail-head d2">DRESS</p>
    <p class="line detail-note d3">summer casual, bare feet welcome</p>
    <p class="line detail-head d4">Cocktail food provided</p>
    <p class="line detail-note d5">BYO but only if you insist</p>
    <p class="line detail-head d6">RSVP</p>
    <p class="line detail-note d7">for catering would be nice.</p>
    <svg class="phone-icon" viewBox="0 0 26 30" aria-hidden="true">
      <rect x="5" y="2" width="14" height="24" rx="2" fill="none" stroke="#fff" stroke-width="1.6"/>
      <line x1="10" y1="22" x2="14" y2="22" stroke="#fff" stroke-width="1.6" stroke-linecap="round"/>
    </svg>
    <p class="line text-us">TEXT US before Xmas please.</p>
    <div class="back-rule r1"></div>
    <p class="line contacts">Mark | +61 400 555 018 &nbsp;or&nbsp; Lisa | +61 400 555 018</p>
    <div class="back-rule r2"></div>
    <p class="line bring-friends">If you have some friends or neighbours that you like to hang out with, we would love to meet.<br>Bring them with you.</p>
  </section>
</body>
</html>
```